Vorlage für ein Workbook
Zielgruppe
Coaching und Beratung
Aufgabenstellung
Es soll eine Vorlage für ein Workbook erstellt werden, das ich dann selbst mit Inhalten füllen kann.. evtl. mit Canvas oder wie auch immer....
Es ist ein 12 Wochenkurs, d.h. ich brauche 1 Titelseite für jede Woche, die ich dann paste und copy machen kann und beschriften kann, sowie eine Vorlage für die einzelnen Seiten des Workbooks. Das Workbook in pdf Format muss auch online ausgefüllt werden können.
Design angepasst an Landingpage

```html
<!DOCTYPE html>
<html lang="en">
<head>
<meta charset="UTF-8">
<title>Part Cover – Workbook</title>
<link href="https://fonts.googleapis.com/css2?family=Cinzel:wght@400&display=swap" rel="stylesheet">
<style>
  :root {
    --paper: #ffffff;
    --taupe: #c4bdb4;
    --taupe-line: #cfc8c0;
    --taupe-soft: #ebe7e2;
    --ink: #111111;
    --highlight: #f3efea;
  }
  html, body {
    margin: 0;
    padding: 0;
    overflow: hidden;
    background: var(--paper);
  }
  .page {
    position: relative;
    width: 849px;
    height: 1200px;
    overflow: hidden;
    background: var(--paper);
  }
  .page-art {
    position: absolute;
    inset: 0;
    width: 849px;
    height: 1200px;
  }
  .part-title {
    position: absolute;
    top: 360px;
    left: 232px;
    width: 400px;
    margin: 0;
    text-align: center;
    font-family: "Cinzel", serif;
    font-weight: 400;
    font-size: 50px;
    letter-spacing: 1px;
    color: var(--taupe);
    line-height: 1;
  }
  .part-subtitle {
    position: absolute;
    top: 447px;
    left: 154px;
    width: 500px;
    margin: 0;
    text-align: center;
    font-family: "Cinzel", serif;
    font-weight: 400;
    font-size: 28px;
    line-height: 34px;
    color: var(--ink);
  }
</style>
</head>
<body>
  <main class="page">
    <svg class="page-art" viewBox="0 0 849 1200" xmlns="http://www.w3.org/2000/svg" aria-hidden="false">
      <!-- top wave band -->
      <path class="top-band" fill="var(--taupe)"
        d="M0 0 H832 C800 90 690 150 520 182 C420 200 330 200 250 222 C130 255 40 330 0 418 Z"/>
      <g class="top-band-lines" fill="none" stroke="var(--highlight)" stroke-width="2">
        <path d="M0 62 C80 40 170 40 250 110 C300 150 360 165 410 120 C450 80 480 20 500 0"/>
        <path d="M0 140 C100 115 190 130 260 195 C320 245 380 262 430 230 C520 170 600 60 720 0"/>
      </g>

      <!-- flowing lines, lower right -->
      <g class="flow-lines" fill="none" stroke="var(--taupe-line)" stroke-width="2">
        <path d="M849 560 C780 640 680 630 600 650 C510 675 480 740 485 850 C490 980 470 1100 380 1200"/>
        <path d="M849 785 C800 810 700 795 640 805 C580 815 560 860 562 960 C564 1060 560 1130 560 1200" stroke-width="3"/>
        <path d="M849 910 C790 900 720 850 650 850 C605 850 600 890 605 960 C612 1060 640 1130 670 1200"/>
      </g>

      <!-- botanical line drawing placeholder -->
      <path class="botanical-area" role="img" aria-label="Fine line drawing of a leafy branch"
        fill="var(--taupe-soft)"
        d="M0 960 C60 900 120 820 200 780 C260 750 300 760 350 850 C330 900 280 930 230 980 C170 1040 160 1120 120 1200 H0 Z"/>
    </svg>

    <h1 class="part-title">Part Cover</h1>
    <p class="part-subtitle">Please change this text with<br>your own words</p>
  </main>
</body>
</html>
```